Quimby's Yard & Garden Center Business Card Update

I need an updated Business card design for my Lawn and Garden Center. We do Landscaping installs, Lawn Mowing, Snow Removal and also have a Garden Center Retail Division. I uploaded a few of our previous business cards to give an idea of what we are starting with. The main goal of this update is to simplify and modernize the business card, not all of the services that are on the previous cards has to be on the new one but I would still like to highlight our main services. There is also a sample of our logo that Can be used in the design.

Industry/Entity Type

Landscaping

Contact Information for Business Card

Morris Quimby
Morris@Quimbysyardandgarden.example
Business (555) 201-7784
Cell (555) 318-6092

Colors

Designer to choose colors to be used in the design.

Requirements
Must have
• Services Provided :
• Landscaping
• Lawn Maintenance
• Snow Removal
• Garden Center

```html
<!DOCTYPE html>
<html lang="en">
<head>
<meta charset="utf-8">
<title>Quimby's Yard & Garden Center – Business Card</title>
<link href="https://fonts.googleapis.com/css2?family=Montserrat:ital,wght@0,400;0,600;0,700;1,400&family=Yellowtail&display=swap" rel="stylesheet">
<style>
  :root{
    --page:#e6e6e6;
    --white:#ffffff;
    --forest:#2b5028;
    --forest-deep:#213f1f;
    --leaf:#558a4d;
    --ink:#111111;
  }
  *{box-sizing:border-box;margin:0;padding:0}
  html,body{width:1200px;height:1200px;overflow:hidden}
  body{background:var(--page);font-family:"Montserrat",Arial,sans-serif;position:relative}
  .card{position:absolute;left:186px;width:828px;height:490px;border-radius:56px;overflow:hidden;background:var(--white)}
  .card-front{top:66px}
  .card-back{top:609px}
  .card-art{position:absolute;inset:0;width:100%;height:100%}
  .brand-name{position:absolute;left:0;width:100%;text-align:center;font-weight:700;color:var(--forest);letter-spacing:1px}
  .front-brand{top:148px;font-size:84px;width:828px}
  .tagline{position:absolute;font-family:"Yellowtail","Brush Script MT",cursive;text-align:center}
  .front-tagline{left:0;width:828px;top:450px;font-size:24px;color:var(--white)}
  .person{position:absolute;left:45px;top:94px;color:var(--white)}
  .person-name{font-size:31px;font-weight:700;line-height:1.1}
  .person-role{font-size:24px;font-style:italic;margin-top:6px}
  .contacts{position:absolute;left:45px;top:200px;list-style:none;color:var(--white)}
  .contact{display:flex;align-items:center;height:30px;font-size:16px;margin-bottom:14px}
  .contact svg{width:30px;height:30px;margin-right:17px;flex:none}
  .contact-address{align-items:flex-start;height:auto;line-height:1.25}
  .company{position:absolute;left:450px;width:394px;top:0;text-align:center;color:var(--ink)}
  .back-brand{font-size:46px;top:60px;color:var(--forest)}
  .back-tagline{left:0;width:100%;top:152px;font-size:19px;color:var(--forest)}
  .site{position:absolute;left:130px;top:192px;display:flex;align-items:center;font-size:12px;color:var(--forest);text-align:left;line-height:1.25}
  .site svg{width:16px;height:20px;margin-right:6px}
  .legal{position:absolute;left:0;width:100%;top:240px;font-weight:700;font-size:16px;line-height:1.15}
  .legal small{display:block;font-weight:400;font-size:11px}
  .rule{position:absolute;height:1.5px;background:var(--forest)}
  .rule-legal{left:104px;width:186px;top:302px}
  .services-title{position:absolute;left:0;width:100%;top:334px;font-weight:700;font-size:19px;color:var(--forest)}
  .rule-services{left:94px;width:193px;top:360px}
  .services{position:absolute;left:0;width:100%;top:367px;font-size:15px;line-height:1.3}
  .dot{display:inline-block;width:6px;height:6px;border-radius:50%;background:var(--forest);vertical-align:middle;margin:0 5px}
</style>
</head>
<body>

<section class="card card-front">
  <svg class="card-art" viewBox="0 0 828 490" preserveAspectRatio="none" aria-hidden="true">
    <path d="M0 351 C30 372 55 387 81 387 C140 387 170 333 217 333 C270 333 340 414 403 414 C460 414 480 358 531 358 C600 358 650 426 705 426 C760 426 800 390 828 364 L828 490 L0 490 Z" fill="var(--leaf)"/>
    <path d="M12 487 C50 465 90 443 143 443 C200 443 225 415 248 415 C290 415 320 446 372 446 C430 446 470 435 527 435 C600 435 660 467 713 467 C760 467 800 462 828 455 L828 490 L0 490 Z" fill="var(--forest-deep)"/>
  </svg>
  <div class="brand-name front-brand">Quimby's</div>
  <div class="tagline front-tagline">Where Gardens Grow..</div>
</section>

<section class="card card-back">
  <svg class="card-art" viewBox="0 0 828 490" preserveAspectRatio="none" aria-hidden="true">
    <path d="M386 0 L450 0 C470 20 478 40 474 70 C468 120 491 150 491 186 C491 230 435 280 435 336 C435 380 447 400 447 416 C447 440 444 470 444 490 L0 490 L0 0 Z" fill="var(--leaf)"/>
    <path d="M0 0 L386 0 C388 30 400 40 400 70 C400 120 376 160 376 192 C376 240 410 270 410 323 C410 380 385 400 368 430 C360 450 365 470 378 490 L0 490 Z" fill="var(--forest)"/>
  </svg>

  <div class="person">
    <h1 class="person-name">Morris Quimby</h1>
    <p class="person-role">Manager</p>
  </div>

  <ul class="contacts">
    <li class="contact">
      <svg viewBox="0 0 30 30" fill="none" stroke="#fff" stroke-width="2" stroke-linecap="round" stroke-linejoin="round"><path d="M6 3 L10 3 L12 9 L9 11 C10 15 14 19 18 20 L20 17 L26 19 L26 23 C26 25 24 27 22 27 C12 26 4 18 3 8 C3 5 4 3 6 3 Z"/><path d="M18 6 a6 6 0 0 1 6 6"/><path d="M18 2 a10 10 0 0 1 10 10"/></svg>
      (555) 318-6092
    </li>
    <li class="contact">
      <svg viewBox="0 0 30 30" fill="none" stroke="#fff" stroke-width="2"><rect x="2" y="3" width="6" height="24" rx="2"/><rect x="10" y="5" width="18" height="22" rx="2"/><rect x="14" y="9" width="10" height="5"/><path d="M14 18h2M18 18h2M22 18h2M14 22h2M18 22h2M22 22h2"/></svg>
      (555) 201-7784
    </li>
    <li class="contact">
      <svg viewBox="0 0 30 30" fill="none" stroke="#fff" stroke-width="2" stroke-linejoin="round"><rect x="2" y="6" width="26" height="19"/><path d="M2 6 L15 17 L28 6 M2 25 L12 15 M28 25 L18 15"/></svg>
      Morris@Quimbysyardandgarden.example
    </li>
    <li class="contact contact-address">
      <svg viewBox="0 0 30 30" fill="none" stroke="#fff" stroke-width="2" stroke-linejoin="round"><path d="M15 15 C11 10 10 8 10 6 a5 5 0 0 1 10 0 C20 8 19 10 15 15 Z"/><circle cx="15" cy="6" r="1.6"/><path d="M8 11 L2 15 L2 28 L28 28 L28 15 L22 11 M2 15 L15 23 L28 15 M2 28 L12 21 M28 28 L18 21"/></svg>
      <span>27 Orchard Lane<br>Maplewood, OH 45999</span>
    </li>
  </ul>

  <div class="company">
    <div class="brand-name back-brand">Quimby's</div>
    <div class="tagline back-tagline">Where Gardens Grow..</div>
    <div class="site">
      <svg viewBox="0 0 16 20" fill="none" stroke="var(--forest)" stroke-width="1.4"><path d="M8 19 C4 13 2 10 2 7 a6 6 0 0 1 12 0 C14 10 12 13 8 19 Z"/><circle cx="8" cy="7" r="2.2"/></svg>
      <span>4820 CO. RD. K<br>Maplewood, OH 45999</span>
    </div>
    <p class="legal">Quimby's Yard &amp; Garden Center<small>And</small>Lawn Service, LLC</p>
    <div class="rule rule-legal"></div>
    <h2 class="services-title">Services Provided :</h2>
    <div class="rule rule-services"></div>
    <p class="services">Landscaping<span class="dot"></span>Lawn Maintenance<br>Snow Removal<span class="dot"></span>Garden Center</p>
  </div>
</section>

</body>
</html>
```